Design a Shirt Hang Tag for a brand new streetwear company

We need a hang tag for our apparel. This will be attached and shipper with every shirt, hat, and hoodie. We make streetwear/urban apparel. For a feel of our products see http://loomferal.co

We'd like to see something die cut with a shape that isn't a rectangle.
Looking for a design that embodies "Savage". We are looking for something bold and fun. Our colors usually consist of black. white, and red, but if you feel like doing something else that you feel could fit our brand,go for it. Were savage, we don't want normal.

Target Market(s)

inner city, age 13-29, multi-cultural

Industry/Entity Type

Clothing

Font styles to use
Sans Serif
Other font styles liked:
• artist's choice

Colors
ec1f27
ffffff
000000

Requirements
Must have
• site url: www.loomferal.co
• Band Name: Loom Feral
• Double sided tag
• Die cut design

```html
<!DOCTYPE html>
<html lang="en">
<head>
<meta charset="utf-8">
<title>Loom Feral — Hang Tag, Front and Back</title>
<link rel="stylesheet" href="https://fonts.googleapis.com/css2?family=Oswald:wght@600&family=Great+Vibes&display=swap">
<style>
  :root {
    --paper: #ffffff;
    --ink: #000000;
    --wood-light: #e0a865;
    --wood-mid: #c98a4e;
    --wood-dark: #8a4f22;
    --bark: #5a2e12;
    --script-ink: #3a1d0c;
  }
  html, body {
    margin: 0;
    padding: 0;
    overflow: hidden;
    background: var(--paper);
  }
  .canvas {
    position: relative;
    width: 853px;
    height: 1200px;
    background: var(--paper);
    overflow: hidden;
  }
  .tag {
    position: absolute;
    width: 600px;
    height: 520px;
  }
  .tag--front { left: 122px; top: 72px; }
  .tag--back  { left: 112px; top: 622px; }

  .tag__shape {
    position: absolute;
    inset: 0;
    width: 100%;
    height: 100%;
    filter: drop-shadow(4px 6px 6px rgba(0,0,0,0.25));
  }
  .tag__hole {
    position: absolute;
    left: 289px;
    top: 58px;
    width: 44px;
    height: 18px;
    border-radius: 9px;
    background: var(--paper);
    border: 1px solid var(--bark);
  }

  .brand {
    position: absolute;
    left: 0;
    width: 100%;
    margin: 0;
    text-align: center;
    font-family: "Oswald", sans-serif;
    font-weight: 600;
    color: var(--ink);
    text-transform: uppercase;
    line-height: 1;
    letter-spacing: 0;
    white-space: nowrap;
  }
  .tag--front .brand { top: 222px; font-size: 92px; padding-left: 22px; box-sizing: border-box; }
  .tag--back  .brand { top: 128px; font-size: 50px; padding-left: 14px; box-sizing: border-box; }

  .url {
    position: absolute;
    left: 0;
    width: 100%;
    margin: 0;
    text-align: center;
    font-family: "Great Vibes", cursive;
    font-size: 52px;
    line-height: 1;
    color: var(--script-ink);
    white-space: nowrap;
    box-sizing: border-box;
  }
  .tag--front .url { top: 420px; padding-left: 22px; }
  .tag--back  .url { top: 424px; padding-left: 14px; }

  .write-in {
    position: absolute;
    left: 118px;
    top: 235px;
    width: 379px;
    height: 178px;
    background: var(--paper);
    border: 2px solid var(--ink);
    border-radius: 28px;
    box-shadow: 0 0 0 4px var(--paper);
  }
</style>
</head>
<body>
<main class="canvas">

  <section class="tag tag--front" aria-label="Hang tag front">
    <svg class="tag__shape" viewBox="0 0 600 520" role="img" aria-label="Die-cut tag shaped like a cross-section of a tree trunk with growth rings and bark edge">
      <defs>
        <radialGradient id="woodFront" cx="52%" cy="50%" r="55%">
          <stop offset="0%" stop-color="var(--wood-light)"/>
          <stop offset="70%" stop-color="var(--wood-mid)"/>
          <stop offset="92%" stop-color="var(--wood-dark)"/>
          <stop offset="100%" stop-color="var(--bark)"/>
        </radialGradient>
      </defs>
      <path fill="url(#woodFront)" d="M110 60 C170 30 240 28 300 24 C370 20 440 30 500 70 C555 110 590 170 588 250 C586 330 560 400 500 450 C440 500 360 515 290 512 C210 508 140 490 95 440 C55 395 40 340 42 270 C44 200 60 130 30 110 C50 85 80 75 110 60 Z"/>
    </svg>
    <span class="tag__hole"></span>
    <h1 class="brand">Loom Feral</h1>
    <p class="url">www.loomferal.co</p>
  </section>

  <section class="tag tag--back" aria-label="Hang tag back">
    <svg class="tag__shape" viewBox="0 0 600 520" role="img" aria-label="Die-cut tag shaped like a cross-section of a tree trunk with growth rings and bark edge">
      <defs>
        <radialGradient id="woodBack" cx="52%" cy="50%" r="55%">
          <stop offset="0%" stop-color="var(--wood-light)"/>
          <stop offset="70%" stop-color="var(--wood-mid)"/>
          <stop offset="92%" stop-color="var(--wood-dark)"/>
          <stop offset="100%" stop-color="var(--bark)"/>
        </radialGradient>
      </defs>
      <path fill="url(#woodBack)" d="M110 60 C170 30 240 28 300 24 C370 20 440 30 500 70 C555 110 590 170 588 250 C586 330 560 400 500 450 C440 500 360 515 290 512 C210 508 140 490 95 440 C55 395 40 340 42 270 C44 200 60 130 30 110 C50 85 80 75 110 60 Z"/>
    </svg>
    <span class="tag__hole"></span>
    <h2 class="brand">Loom Feral</h2>
    <div class="write-in" aria-label="Blank area for size and price"></div>
    <p class="url">www.loomferal.co</p>
  </section>

</main>
</body>
</html>
```